New Wedding Decor Web Design Project - GUARANTEED PAYMENT

We need to have a business website for a brand new wedding decor & events company, Lirovelle. We have just established our logo and would love to use this logo on the website.

Because this is a new business venture, we do not have too many pictures to post online. It'd be exciting what your creativity can bring us!

Our website is: www.Lirovelle.ca

Target Market(s)

Our clientele demographic is targeted to brides and bridesmaids in their 20-30 years old.

Industry/Entity Type

Wedding

Requirements
Must have
• - Professional, elegant and artistic look
- Modern feeling
- Very catchy flash intro page
- Ability to show Chatterbook posts
Nice to have
• - Easy to navigate, crisp and clean
- Live vocaline messaging or online messaging

I would like to have navigation pages like: Lirovelle Brand, Collections, Features, Contact Us, etc.

Each page I want it to be clean and easy to read. Something like the following website: http://www.pardunetho.com/

We offer:
BACKDROPS
HEAD, CAKE & RECEIVING TABLES DECOR
CHAIRCOVERS
TABLE CLOTHS & OVERLAYS
NAPKINS
CENTREPIECES
CEREMONY SET-UP
CANDELABRA
CRYSTAL GLOBES
LED LIGHTING
CUSTOM DESIGN AISLE RUNNERS
CAKE STANDS
MONEY BOX
CHARGERS
GOBO LIGHTING
Should not have
• - traditional, old style website
- very static (dull)
- too many images or busy layout
- no "standardized" website templates such as: www.brintaq.com/gallery/weddings

```html
<!DOCTYPE html>
<html lang="en">
<head>
<meta charset="utf-8">
<title>Lirovelle Wedding Events</title>
<link href="https://fonts.googleapis.com/css2?family=Tinos:wght@400;700&display=swap" rel="stylesheet">
<style>
  :root {
    --page-bg: #f6f6f8;
    --lavender: #d9d2f0;
    --lavender-deep: #b9a3dd;
    --nav-grey: #c3c3c4;
    --nav-active: #ababac;
    --nav-edge: #8e8e90;
    --link-pink: #e0197d;
    --panel-white: #f7f8f8;
    --ink: #000000;
    --logo-grey: #8a8a8a;
    --info-navy: #1a2e6e;
    --info-purple: #9b3fd6;
    --faint: #e9e8f2;
    --footer-bg: #07070d;
    --footer-white: #f2f2f2;
    --footer-blue: #2c4a9a;
    --footer-gold: #b3a21e;
    --social-gold: #c9b01f;
    --icon-blue: #3b5592;
  }
  * { margin: 0; padding: 0; box-sizing: border-box; }
  html, body { width: 1200px; height: 1024px; overflow: hidden; }
  body {
    position: relative;
    font-family: "Tinos", "Times New Roman", serif;
    background:
      radial-gradient(ellipse 700px 260px at 1100px 700px, #ebe4f8 0%, rgba(235,228,248,0) 100%),
      linear-gradient(180deg, #d6cdee 0%, #ecebf4 6%, #f1f1f5 18%, var(--page-bg) 30%, var(--page-bg) 100%);
  }
  .sky-wave { position: absolute; left: 0; top: 0; width: 1200px; height: 300px; }

  .brand-mark { position: absolute; left: 47px; top: 47px; width: 135px; height: 105px;
    border-radius: 50%; background: radial-gradient(circle at 55% 45%, #f7b6d6 0%, #e8479a 55%, rgba(232,71,154,0) 75%); }
  .brand-name { position: absolute; left: 44px; top: 146px; font-size: 52px; color: var(--logo-grey); line-height: 1; }
  .brand-tag { position: absolute; left: 182px; top: 202px; font-size: 18px; color: var(--logo-grey); letter-spacing: 1px; line-height: 1; }

  .main-nav { position: absolute; left: 42px; top: 228px; width: 579px; height: 64px;
    background: var(--nav-grey); border-left: 4px solid var(--nav-edge); }
  .main-nav a { position: absolute; top: 0; height: 64px; line-height: 70px; font-size: 21px;
    color: var(--link-pink); text-decoration: none; }
  .main-nav a.is-active { background: var(--nav-active); padding: 0 15px; left: 10px; }

  .intro-panel { position: absolute; left: 42px; top: 292px; width: 579px; height: 554px; background: var(--panel-white); }
  .welcome { position: absolute; left: 0; width: 579px; top: 76px; text-align: center; font-size: 50px; font-weight: 400; color: var(--ink); }
  .intro-logo { position: absolute; left: 106px; top: 196px; font-size: 72px; color: var(--logo-grey); line-height: 1; }
  .intro-tag { position: absolute; left: 282px; top: 275px; font-size: 25px; color: var(--logo-grey); letter-spacing: 1px; line-height: 1; }
  .intro-note { position: absolute; left: 175px; top: 383px; font-size: 17px; line-height: 22px; color: var(--ink); }

  .divider { position: absolute; left: 621px; top: 228px; width: 3px; height: 618px; background: var(--lavender-deep); }

  .page-tab { position: absolute; left: 622px; top: 333px; width: 46px; height: 63px;
    background: var(--lavender); border-radius: 0 24px 24px 0; }
  .page-tab .tab-square { position: absolute; left: 6px; top: 20px; width: 15px; height: 15px; background: var(--icon-blue); }
  .page-tab .tab-label { position: absolute; left: 20px; top: 14px; writing-mode: vertical-rl; font-size: 17px; color: #3a3a55; }

  .ornament { position: absolute; }
  .ornament-corner { left: 1014px; top: 281px; width: 164px; height: 153px;
    background: radial-gradient(ellipse at 70% 35%, rgba(185,163,221,0.55) 0%, rgba(185,163,221,0) 70%); }
  .ornament-base { left: 455px; top: 691px; width: 328px; height: 155px;
    background: radial-gradient(ellipse at 50% 80%, rgba(185,163,221,0.5) 0%, rgba(185,163,221,0) 70%); }

  .info { position: absolute; left: 701px; top: 300px; width: 380px; }
  .info h2 { text-align: center; font-weight: 400; font-size: 28px; color: var(--info-navy); margin-left: -18px; }
  .info .lede { margin-top: 6px; font-size: 19px; line-height: 23px; color: var(--info-purple); text-indent: 42px; }
  .info .contact { margin-top: 23px; font-size: 19px; line-height: 23px; color: var(--info-purple); }
  .info h3 { margin-top: 73px; font-weight: 400; font-size: 19px; color: var(--faint); padding-left: 84px; }
  .info .note { margin-top: 27px; font-size: 19px; line-height: 23.4px; color: var(--ink); }
  .info .note + .note { margin-top: 23px; }

  .site-footer { position: absolute; left: 0; top: 875px; width: 1200px; height: 149px;
    background: repeating-linear-gradient(135deg, #0b0b12 0 3px, var(--footer-bg) 3px 6px); }
  .contact-list { position: absolute; left: 68px; top: 13px; list-style: none; font-size: 17px; line-height: 21px; color: var(--footer-white); }
  .sitemap { position: absolute; left: 68px; top: 87px; font-size: 17px; color: var(--footer-blue); text-decoration: none; }
  .copyright { position: absolute; left: 68px; top: 113px; font-size: 18px; color: var(--footer-gold); }
  .footer-rule { position: absolute; left: 622px; top: 12px; width: 1px; height: 86px; background: #d8d8d8; }
  .social { position: absolute; left: 642px; top: 33px; display: flex; align-items: center; }
  .social-square { width: 26px; height: 24px; background: var(--icon-blue); margin-right: 10px; }
  .social-text { font-size: 19px; color: var(--social-gold); margin-top: 6px; }
</style>
</head>
<body>
  <svg class="sky-wave" viewBox="0 0 1200 300" aria-hidden="true">
    <defs>
      <linearGradient id="wave-fill" x1="0" y1="0" x2="1" y2="0">
        <stop offset="0" stop-color="#ffffff" stop-opacity="0.55"/>
        <stop offset="1" stop-color="#ffffff" stop-opacity="0.2"/>
      </linearGradient>
    </defs>
    <path d="M0 70 C 300 30, 600 150, 900 90 S 1150 60, 1200 80 L1200 0 L0 0 Z" fill="#cfc3ec" opacity="0.35"/>
    <path d="M500 180 C 700 120, 900 240, 1200 200 L1200 300 L500 300 Z" fill="url(#wave-fill)"/>
  </svg>

  <header class="site-header">
    <div class="brand-mark" role="img" aria-label="Pink peony flower illustration"></div>
    <div class="brand-name">Lirovelle</div>
    <div class="brand-tag">wedding events</div>
  </header>

  <nav class="main-nav">
    <a class="is-active" href="#">Home</a>
    <a style="left:151px" href="#">Brand</a>
    <a style="left:241px" href="#">Collections</a>
    <a style="left:369px" href="#">Features</a>
    <a style="left:475px" href="#">Contact Us</a>
  </nav>

  <section class="intro-panel">
    <h1 class="welcome">Welcome To</h1>
    <div class="intro-logo">Lirovelle</div>
    <div class="intro-tag">wedding events</div>
    <p class="intro-note">A Flash intro animated design<br>&nbsp;will be goes here.</p>
  </section>

  <div class="ornament ornament-base" role="img" aria-label="Lavender floral scroll ornament"></div>
  <div class="divider"></div>

  <div class="page-tab">
    <span class="tab-square"></span>
    <span class="tab-label">Page</span>
  </div>

  <div class="ornament ornament-corner" role="img" aria-label="Lavender floral corner ornament"></div>

  <aside class="info">
    <h2>Info</h2>
    <p class="lede">A small introduction about your&nbsp; company will goes here.</p>
    <p class="contact">A small contact details also can&nbsp; be added.</p>
    <h3>Please Read</h3>
    <p class="note">I designed the page to have less images.<br>This page background can be code with HTML/CSS to have very few and small sized images.</p>
    <p class="note">It will reduce page size &amp; the page will lode faster.</p>
  </aside>

  <footer class="site-footer">
    <ul class="contact-list">
      <li>Phone:</li>
      <li>Email:</li>
      <li>Fax:</li>
    </ul>
    <a class="sitemap" href="#">sitemap</a>
    <div class="copyright">lirovelle (C) 2013</div>
    <div class="footer-rule"></div>
    <div class="social">
      <span class="social-square"></span>
      <span class="social-text">We are Social</span>
    </div>
  </footer>
</body>
</html>
```